Every Drawer Neatly Sorted or EDN Organized needs a business card design. EDN Organized is a professi

We need a business card design that is clean, sharp and conveys a sense of organization. I already have a logo.

Target Market(s)

Families (specifically mothers), small business owners, parents, seniors

Industry/Entity Type

Business

Contact Information for Business Card

My website is www.ednorganized-example.com and my Social page page is http://www.socialpage-example.com/everydrawerneatlysorted. The phone number is 555-418-2706 and I want to be listed as Miriel O. Dunsford, Owner

Requirements
Must have
• My logo.

```html
<!DOCTYPE html>
<html lang="en">
<head>
<meta charset="utf-8">
<title>EDN Organized – Business Card</title>
<link rel="stylesheet" href="https://fonts.googleapis.com/css2?family=Raleway:wght@400;500&display=swap">
<style>
  :root {
    --page-bg: #eef0f3;
    --brand-blue: #4b8fd1;
    --brand-blue-deep: #3d82c8;
    --sky: #85c2ec;
    --sky-soft: #a9d3f2;
    --stripe: #7db6e4;
    --row-fill: #bcd8f0;
    --paper: #f3f5f7;
    --owner-blue: #2e6db3;
    --contact-text: #3a7bc0;
    --white: #ffffff;
  }
  * { margin: 0; padding: 0; box-sizing: border-box; }
  html, body {
    width: 1200px; height: 1072px; overflow: hidden;
    background: var(--page-bg);
    font-family: "Raleway", sans-serif;
  }
  .card {
    position: absolute; left: 100px; top: 250px;
    width: 1000px; height: 572px;
    background: var(--paper);
    overflow: hidden;
    box-shadow: 0 12px 30px rgba(40, 60, 90, .18);
  }
  .header-band {
    position: absolute; left: 0; top: 0; width: 100%; height: 250px;
    background: linear-gradient(100deg, var(--brand-blue) 0%, var(--brand-blue-deep) 100%);
  }
  .header-stripe {
    position: absolute; left: 0; top: 250px; width: 100%; height: 22px;
    background: var(--stripe);
  }
  .logo-disc {
    position: absolute; left: 40px; top: -110px; width: 300px; height: 300px;
    border-radius: 50%; background: var(--sky);
    box-shadow: 0 10px 0 rgba(255,255,255,.18);
  }
  .logo-name {
    position: absolute; left: 40px; top: 100px; width: 300px;
    text-align: center; color: var(--white);
    font-weight: 400; font-size: 58px; letter-spacing: 2px;
  }
  .company-name {
    position: absolute; left: 390px; top: 92px; color: var(--white); font-weight: 400;
    white-space: nowrap;
  }
  .company-name .line-top { display: block; font-size: 32px; letter-spacing: 5px; padding-left: 60px; }
  .company-name .line-main { display: block; font-size: 60px; letter-spacing: 22px; line-height: 1.1; }
  .person-box {
    position: absolute; left: 0; top: 292px; width: 370px; height: 140px;
    background: var(--sky); padding: 28px 0 0 28px;
    white-space: nowrap;
  }
  .person-name { color: var(--white); font-size: 32px; font-weight: 500; }
  .person-role { color: var(--owner-blue); font-size: 28px; font-weight: 500; margin-top: 6px; }
  .tab-strip {
    position: absolute; left: 370px; top: 292px; width: 40px; height: 140px;
    background: var(--sky-soft); opacity: .7;
  }
  .connectors { position: absolute; left: 0; top: 0; }
  .contact-list { position: absolute; left: 520px; top: 328px; list-style: none; }
  .contact-row {
    position: relative; height: 48px; width: 460px; margin-bottom: 10px;
    background: var(--row-fill); padding-left: 62px;
    color: var(--contact-text); font-size: 25px; font-weight: 500; line-height: 48px;
    white-space: nowrap;
  }
  .contact-icon {
    position: absolute; left: -6px; top: -2px; width: 52px; height: 52px;
    border-radius: 50%; background: var(--sky-soft);
  }
  .contact-icon svg { position: absolute; left: 14px; top: 14px; }
</style>
</head>
<body>
  <div class="card">
    <div class="header-band"></div>
    <div class="header-stripe"></div>
    <div class="logo-disc"></div>
    <div class="logo-name">EDN</div>
    <div class="company-name">
      <span class="line-top">Every Drawer Neatly</span>
      <span class="line-main">SORTED</span>
    </div>

    <div class="person-box">
      <div class="person-name">Miriel O. Dunsford</div>
      <div class="person-role">Owner</div>
    </div>
    <div class="tab-strip"></div>

    <svg class="connectors" width="1000" height="572" viewBox="0 0 1000 572" aria-hidden="true">
      <g fill="none" stroke="#b9d6ef" stroke-width="4">
        <path d="M410 318 C460 318 475 352 520 352"/>
        <path d="M410 362 C460 362 475 410 520 410"/>
        <path d="M410 406 C460 406 475 468 520 468"/>
      </g>
    </svg>

    <ul class="contact-list">
      <li class="contact-row">
        <span class="contact-icon">
          <svg width="24" height="24" viewBox="0 0 24 24" fill="none" stroke="#ffffff" stroke-width="2">
            <circle cx="12" cy="12" r="10"/><path d="M2 12h20M12 2c3 3 3 17 0 20M12 2c-3 3-3 17 0 20"/>
          </svg>
        </span>www.ednorganized-example.com
      </li>
      <li class="contact-row">
        <span class="contact-icon">
          <svg width="24" height="24" viewBox="0 0 24 24"><circle cx="12" cy="12" r="6" fill="#ffffff"/></svg>
        </span>/everydrawerneatlysorted
      </li>
      <li class="contact-row">
        <span class="contact-icon">
          <svg width="24" height="24" viewBox="0 0 24 24" fill="#ffffff">
            <path d="M6.6 10.8a15 15 0 0 0 6.6 6.6l2.2-2.2c.3-.3.7-.4 1-.2 1.1.4 2.3.6 3.6.6.6 0 1 .4 1 1V20c0 .6-.4 1-1 1A17 17 0 0 1 3 4c0-.6.4-1 1-1h3.5c.6 0 1 .4 1 1 0 1.3.2 2.5.6 3.6.1.3 0 .7-.2 1z"/>
          </svg>
        </span>555-418-2706
      </li>
    </ul>
  </div>
</body>
</html>
```